Creative design for PLW Businesscard!

We would like a creative business card for our company The Maple Workshop. We situated in Barcelona and setup software development teams for companies in Belgium, Holland.

Orange is related to Holland.
PLW means cool in Dutch

* An Overview / Background of the Business & Services
o Setup and manage developer teams in Barcelona for for companies
in Holland, Belgium.
* The Target Market / Audience you are trying to reach
o Companies in Holland searching for developers
* Design Specifics; any preferences or ideas for Style, Colour,
Imagery, etc
o Orange, professional, fancy
o The Maple Workshop (PLW) means cool , good, nice

Target Market(s)

Companies in Holland searching for developers

Industry/Entity Type

Business

Contact Information for Business Card

Company name: The Maple Workshop

Name: Joost ter Haarveld

Title: Managing director (not necessary)

Email: joost@themapleworkshop.es

web: www.themapleworkshop.es

Phone: (+34) 932 487 113

Mobile: (+34) 668 302 947

Font styles to use
Other font styles liked:
• Bookman Old Style or Rockwell

Requirements
Must have
• Setup and manage developer teams in Barcelona for for companies
• in Holland, Belgium.

```html
<!DOCTYPE html>
<html lang="en">
<head>
<meta charset="utf-8">
<title>The Maple Workshop – Business Card</title>
<link rel="stylesheet" href="https://fonts.googleapis.com/css2?family=Arimo:wght@400;700&display=swap">
<style>
  :root {
    --page-bg: #d8d4ce;
    --card-top: #f1efec;
    --card-bottom: #dedad4;
    --ink: #2a2724;
    --ink-soft: #3a3633;
    --ink-muted: #5a534e;
    --orange: #e3683c;
    --orange-light: #ef8b5d;
    --on-orange: #f7ece6;
    --icon: #b9aea6;
  }
  * { margin: 0; padding: 0; box-sizing: border-box; }
  html, body {
    width: 1200px; height: 970px; overflow: hidden;
    background: var(--page-bg);
    font-family: "Arimo", Arial, sans-serif;
  }
  .card {
    position: absolute; left: 80px; top: 189px;
    width: 1040px; height: 592px;
    background: linear-gradient(160deg, var(--card-top), var(--card-bottom));
    box-shadow: 0 10px 30px rgba(0,0,0,.18);
    overflow: hidden;
  }
  .fruit-art {
    position: absolute; left: 0; top: 165px;
    width: 470px; height: 427px;
    background: linear-gradient(150deg, var(--orange-light), var(--orange));
    opacity: .92;
  }
  .brand-mark {
    position: absolute; right: 48px; top: 78px;
    font-size: 172px; font-weight: 700; line-height: 1;
    color: var(--ink); letter-spacing: 4px;
  }
  .person { position: absolute; left: 52px; top: 292px; color: var(--on-orange); }
  .person-name { font-size: 34px; font-weight: 700; line-height: 1.05; }
  .person-title { font-size: 28px; color: var(--ink-soft); line-height: 1.05; }
  .contacts { position: absolute; left: 52px; top: 405px; list-style: none; }
  .contacts li {
    display: flex; align-items: center; gap: 16px;
    height: 37px; font-size: 28px; color: var(--on-orange);
  }
  .contacts svg { width: 30px; height: 30px; flex: none; }
  .company {
    position: absolute; right: 48px; top: 356px;
    font-size: 42px; font-weight: 700; color: var(--ink);
  }
  .company .accent { color: var(--orange); }
  .tagline {
    position: absolute; right: 48px; top: 414px; width: 480px;
    font-size: 18px; line-height: 23px; text-align: right; color: var(--ink-muted);
  }
  .address {
    position: absolute; right: 48px; top: 480px;
    font-size: 28px; line-height: 35px; text-align: right; color: var(--ink);
  }
</style>
</head>
<body>
  <div class="card">
    <div class="fruit-art" role="img" aria-label="Large orange fruit with a green leaf illustration"></div>

    <div class="brand-mark">PLW</div>

    <div class="person">
      <div class="person-name">Joost ter Haarveld</div>
      <div class="person-title">Managing director</div>
    </div>

    <ul class="contacts">
      <li>
        <svg viewBox="0 0 30 30" aria-hidden="true"><rect width="30" height="30" fill="var(--icon)"/><rect x="10" y="5" width="10" height="20" rx="2" fill="none" stroke="#fff" stroke-width="2"/><circle cx="15" cy="22" r="1.2" fill="#fff"/></svg>
        (+34) 668 302 947
      </li>
      <li>
        <svg viewBox="0 0 30 30" aria-hidden="true"><rect width="30" height="30" fill="var(--icon)"/><path d="M6 12c0-4 18-4 18 0v2h-5v-2h-8v2H6z" fill="#fff"/><rect x="8" y="15" width="14" height="9" rx="1" fill="#fff"/></svg>
        (+34) 932 487 113
      </li>
      <li>
        <svg viewBox="0 0 30 30" aria-hidden="true"><rect width="30" height="30" fill="var(--icon)"/><rect x="5" y="8" width="20" height="14" fill="none" stroke="#fff" stroke-width="2"/><path d="M5 8l10 8 10-8" fill="none" stroke="#fff" stroke-width="2"/></svg>
        joost@themapleworkshop.es
      </li>
      <li>
        <svg viewBox="0 0 30 30" aria-hidden="true"><rect width="30" height="30" fill="var(--icon)"/><circle cx="15" cy="15" r="9" fill="none" stroke="#fff" stroke-width="1.8"/><ellipse cx="15" cy="15" rx="4" ry="9" fill="none" stroke="#fff" stroke-width="1.5"/><path d="M6 15h18" stroke="#fff" stroke-width="1.5"/></svg>
        www.themapleworkshop.es
      </li>
    </ul>

    <div class="company">The <span class="accent">Maple</span> Workshop</div>

    <p class="tagline">Setup and manage developer teams in Barcelona<br>for companies in Holland, Belgium.</p>

    <div class="address">
      Carrer de Vilanova 74, principal<br>
      08011 Barcelona, España
    </div>
  </div>
</body>
</html>
```